Website design for a construction company

The logo and the copies of all the 3 pages are attached below. I don't have a preference in colors but I would ideally like to use the colors on my logo, dark teal (secondary) and copper (primary).

Company Name: Brackwyn Group

Location: London, UK

Business Overview:

Brackwyn Group is a comprehensive construction company based in London, specializing in a wide range of construction services. We cater to various sectors, providing services including electrical work, painting and decorating, plastering, plumbing, carpentry, kitchen and bathroom installations, loft conversions, and extensions. Our team is known for its skilled craftsmanship, attention to detail, and commitment to quality.

What "BRACKWYN" stands for:

Our company name, 'BRACKWYN', is derived from Brackwynion, the ancient Greek god of craftsmen, blacksmiths, artisans, sculptors, metals, metallurgy, fire, and volcanoes. Brackwynion was renowned in mythology for his incredible skill in crafting and creating, making him the patron of all craftsmen and artisans. His name is synonymous with the mastery of artisanship and the creation of wondrous, enduring works.

In choosing 'BRACKWYN' as our name, we embody the spirit and skills of Brackwynion. It reflects our commitment to craftsmanship, excellence, and durability in the field of construction. Just as Brackwynion was known for his meticulous work, precision, and innovative creations, our company strives to uphold these qualities in every project we undertake.

Our name is a constant reminder of our dedication to quality, innovation, and the art of building. It symbolizes our endeavor to achieve the highest standards in construction, much like Brackwynion did in his timeless creations. In essence, 'BRACKWYN' is not just our name; it's a representation of our ethos and the high standards we set for ourselves in the construction industry.

Target Audience:

Our primary audience includes homeowners, real estate developers, and commercial clients in London seeking reliable, high-quality construction services.

Unique Selling Points:

Diverse Range of Services: Offering a one-stop solution for all construction needs.

Certified and Experienced: Professional team with a strong focus on delivering certified and compliant work, particularly in electrical services.

Client-Centric Approach: Emphasizing client satisfaction, we tailor our services to meet the unique needs and visions of our clients.

Quality and Reliability: Commitment to high-quality materials, skilled workmanship, and delivering projects on time and within budget.

Website Requirements:

Clean, professional design reflecting the quality and reliability of our services.

User-friendly navigation to easily access information about our services, portfolio, company background, and contact details.

Portfolio section showcasing our past projects with placeholders for images and descriptions.

Integration of a contact form, map for our location, and links to our social media accounts.

Mobile-responsive design to ensure accessibility across various devices.

Purpose of the Website:
The website aims to:

Establish an online presence and credibility in the construction industry.

Provide an informative resource about our services and past projects to potential clients.

Facilitate easy communication and inquiries through an integrated contact system.

Tone and Style:

Professional, informative, and welcoming. The website should convey trustworthiness and expertise in the construction field.

Target Market(s)

homeowners, real estate developers, and commercial clients

Industry/Entity Type

Construction

Number of Pages Required

3 page

Colors

Designer to choose colors to be used in the design.

```html
<!DOCTYPE html>
<html lang="en">
<head>
<meta charset="utf-8">
<title>Brackwyn Group — Construction in London</title>
<link href="https://fonts.googleapis.com/css2?family=Outfit:wght@300;400;500&family=Inter:wght@400;500;600;700&display=swap" rel="stylesheet">
<style>
:root{
  --teal:#0f5550;
  --teal-deep:#0d514c;
  --copper:#b87433;
  --sky:#7bacdb;
  --ink:#1a1a1a;
  --muted:#4a4a4a;
  --line:#e3e3e3;
  --white:#ffffff;
}
*{margin:0;padding:0;box-sizing:border-box}
html,body{width:1200px;height:4167px;overflow:hidden;background:var(--white)}
body{position:relative;font-family:"Inter",sans-serif;color:var(--ink)}
.abs{position:absolute}
.display{font-family:"Outfit",sans-serif;font-weight:400;letter-spacing:-1px}
.brand{display:flex;align-items:center;gap:8px;font-family:"Inter",sans-serif;font-weight:600;color:var(--teal);font-size:22px;letter-spacing:1px}
.brand .mark{width:24px;height:24px;background:var(--copper)}
.topbar{left:94px;top:38px;right:94px;display:flex;justify-content:space-between;align-items:center}
.contacts{display:flex;gap:26px;font-size:11px;font-weight:500;color:var(--teal);align-items:center}
.contacts span{display:flex;align-items:center;gap:8px}
.contacts svg{width:14px;height:14px}
.rule{left:0;width:1200px;height:1px;background:var(--line)}
.nav{left:94px;top:126px;display:flex;gap:38px;font-size:12px;font-weight:500;color:var(--teal)}
.nav .active{color:var(--ink);text-decoration:underline;text-underline-offset:5px;font-weight:600}
.btn{display:flex;align-items:center;justify-content:center;gap:10px;border-radius:4px;font-weight:500}
.btn-copper{background:var(--copper);color:var(--white)}
.register{left:945px;top:116px;width:160px;height:35px;font-size:12px}
.hero-title{left:0;width:1200px;top:250px;text-align:center;font-size:78px;line-height:62px;color:var(--teal)}
.hero-title em{font-style:normal;color:var(--copper)}
.hero-title .u{text-decoration:underline;text-decoration-thickness:3px;text-underline-offset:8px}
.hero-sub{left:0;width:1200px;top:405px;text-align:center;font-size:20px;color:var(--teal);font-weight:500}
.consult{left:488px;top:471px;width:222px;height:45px;font-size:16px}
.hero-photo{left:19px;top:556px;width:1160px;height:334px;background:linear-gradient(180deg,#5d6670,#3c3f44 55%,#8a8580)}
.welcome{left:19px;top:890px;width:1160px;height:362px;background:linear-gradient(180deg,#4b7fb8 0%,#5a8cc2 45%,#2f4f78 100%)}
.welcome h2{position:absolute;left:75px;top:88px;font-size:50px;line-height:50px;color:var(--white)}
.welcome p{position:absolute;left:75px;top:218px;width:1030px;font-size:15px;line-height:27px;color:var(--white)}
.section-title{font-size:52px;color:var(--ink)}
.why-title{left:0;width:1200px;top:1340px;text-align:center}
.why-sub{left:130px;width:940px;top:1410px;text-align:center;font-size:20px;line-height:27px;color:var(--teal)}
.card{top:1516px;width:248px;height:373px;border:1px solid var(--line);border-radius:6px;background:var(--white)}
.card h3{position:absolute;left:20px;top:20px;font-size:39px;line-height:41px;color:var(--ink);font-weight:400}
.card p{position:absolute;left:20px;top:114px;width:200px;font-size:12px;line-height:18px;color:var(--teal)}
.card .photo{position:absolute;left:20px;top:168px;width:208px;height:129px;border-radius:5px}
.card .more{position:absolute;left:20px;top:320px;width:208px;height:34px;font-size:12px;font-weight:600}
.card.featured{background:var(--copper);border-color:var(--copper)}
.card.featured h3,.card.featured p{color:var(--white)}
.card.featured .more{background:var(--white);color:var(--copper)}
.cursor{position:absolute;right:20px;top:38px;width:24px;height:24px}
.svc-title{left:73px;top:2030px;color:var(--teal)}
.svc-sub{left:73px;top:2103px;width:1060px;font-size:20px;line-height:27px;color:var(--teal)}
.slide{top:2208px;height:501px}
.slide-label{top:2730px;font-size:16px;font-weight:600;color:var(--ink)}
.see{top:2730px;font-size:16px;color:var(--teal)}
.arrow{width:32px;height:32px}
.dots{display:flex;gap:16px}
.dots i{width:12px;height:12px;border-radius:50%;background:#9fb6b8}
.dots i.on{background:var(--teal)}
.testi{left:19px;top:2866px;width:1160px;height:521px;background:var(--teal-deep);color:var(--white)}
.testi h2{position:absolute;left:75px;top:90px;font-size:74px;line-height:60px;font-family:"Outfit",sans-serif;font-weight:400;letter-spacing:-1px}
.testi .lead{position:absolute;left:75px;top:224px;width:960px;font-size:20px;line-height:27px}
.testi .quote{position:absolute;left:200px;width:760px;top:328px;text-align:center;font-size:15px;line-height:21px}
.testi .who{position:absolute;left:0;width:1160px;top:389px;text-align:center;font-size:11px}
.testi .dots{position:absolute;left:508px;top:457px}
.testi .dots i{background:#b9c9c8}
.testi .dots i.on{background:var(--white)}
.contact{left:19px;top:3387px;width:1160px;height:413px;background:var(--sky);color:var(--white);text-align:center}
.contact h2{position:absolute;left:0;width:1160px;top:80px;font-size:76px;font-family:"Outfit",sans-serif;font-weight:400;letter-spacing:-1px}
.contact p{position:absolute;left:80px;width:1000px;top:178px;font-size:20px;line-height:27px}
.start{position:absolute;left:476px;top:260px;width:207px;height:60px;background:var(--white);color:var(--teal);font-size:16px;font-weight:600}
.foot-about{left:60px;top:3922px;width:470px;font-size:16px;line-height:27px;color:var(--ink)}
.socials{left:60px;top:4023px;display:flex;gap:18px}
.socials i{width:16px;height:16px;border-radius:50%;border:2px solid var(--ink)}
.foot-contacts{left:60px;top:4063px;display:flex;gap:26px;font-size:11px;font-weight:500;color:var(--ink)}
.foot-contacts span{display:flex;align-items:center;gap:10px}
.foot-contacts svg{width:14px;height:14px}
.foot-links{left:720px;top:3925px;display:grid;grid-template-columns:146px 148px 120px;row-gap:24px;font-size:16px;color:var(--ink)}
.copy{left:60px;top:4134px;font-size:11px;color:var(--ink)}
.legal{right:60px;top:4134px;display:flex;gap:22px;font-size:11px;color:var(--ink)}
</style>
</head>
<body>

<header>
  <div class="abs topbar">
    <div class="brand"><span class="mark"></span>BRACKWYN</div>
    <div class="contacts">
      <span><svg viewBox="0 0 16 16" fill="none" stroke="currentColor" stroke-width="1.4"><rect x="1.5" y="3" width="13" height="10" rx="1"/><path d="M2 4l6 5 6-5"/></svg>brackwyn****@mailbox.com</span>
      <span><svg viewBox="0 0 16 16" fill="none" stroke="currentColor" stroke-width="1.4"><path d="M3 2h3l1.5 3.5-2 1.2a8 8 0 004 4l1.2-2L14 10v3a1 1 0 01-1 1A11 11 0 012 3a1 1 0 011-1z"/></svg>+44 20 *******</span>
      <span><svg viewBox="0 0 16 16" fill="none" stroke="currentColor" stroke-width="1.4"><path d="M8 15s5-5 5-8.5a5 5 0 00-10 0C3 10 8 15 8 15z"/><circle cx="8" cy="6.5" r="1.8"/></svg>London, UK</span>
    </div>
  </div>
  <div class="abs rule" style="top:97px"></div>
  <nav class="abs nav">
    <span class="active">Home</span><span>About Us</span><span>Our Service</span><span>Portfolio</span><span>Contact</span>
  </nav>
  <div class="abs btn btn-copper register">Register Now
    <svg width="10" height="10" viewBox="0 0 10 10" fill="none" stroke="#fff" stroke-width="1.5"><path d="M2 8l6-6M3 2h5v5"/></svg></div>
  <div class="abs rule" style="top:171px"></div>
</header>

<section>
  <h1 class="abs display hero-title">Building Your <em>Dreams</em><br>Into <em class="u">Reality</em></h1>
  <p class="abs hero-sub">Expert Craftsmanship Meets Unmatched Reliability in the Heart of London</p>
  <div class="abs btn btn-copper consult">Consultation Now
    <svg width="12" height="12" viewBox="0 0 12 12" fill="none" stroke="#fff" stroke-width="1.5"><path d="M2 6h8M7 3l3 3-3 3"/></svg></div>
  <div class="abs hero-photo" role="img" aria-label="City construction sites with lit building frames at dusk"></div>
  <div class="abs welcome" role="img" aria-label="Tower cranes against a blue evening sky">
    <h2 class="display">Welcome To<br>Brackwyn Group</h2>
    <p>Where Construction Meets Excellence.&nbsp; Based in London, we are committed to transforming your spaces into exceptional places. Our team is dedicated to delivering the highest quality in every project, attending to every detail with precision and care."</p>
  </div>
</section>

<section>
  <h2 class="abs display section-title why-title">Why Choose Us?</h2>
  <p class="abs why-sub">Discover how we can bring your vision to life, covering every aspect of construction from the initial design to the final touches</p>

  <div class="abs card" style="left:113px">
    <h3 class="display">Our<br>Expertise</h3>
    <p>Leveraging over 10 years of experience</p>
    <div class="photo" role="img" aria-label="Construction worker in safety vest on site" style="background:linear-gradient(135deg,#7a8590,#4c555c)"></div>
    <div class="btn btn-copper more">Read More</div>
  </div>
  <div class="abs card featured" style="left:476px">
    <h3 class="display">Quality<br>Assurance</h3>
    <svg class="cursor" viewBox="0 0 24 24"><path d="M4 3l16 7-7 2-2 7z" fill="#fff"/></svg>
    <p>Quality is not just a promise, but a practice</p>
    <div class="photo" role="img" aria-label="Team working at computers in an office" style="background:linear-gradient(135deg,#c9ccd0,#5f6468)"></div>
    <div class="btn more">Read More</div>
  </div>
  <div class="abs card" style="left:838px">
    <h3 class="display">Certificied<br>Excellence</h3>
    <p>Your safety and satisfaction are our top priorities.</p>
    <div class="photo" role="img" aria-label="Signed certificate document" style="background:linear-gradient(135deg,#f4f4f4,#dcdcdc)"></div>
    <div class="btn btn-copper more">Read More</div>
  </div>
</section>

<section>
  <h2 class="abs display section-title svc-title">Our Service</h2>
  <p class="abs svc-sub">Our Services – Tailored to Your Needs. Discover how we can bring your vision to life, covering every aspect of construction from the initial design to the final touches</p>

  <div class="abs slide" role="img" aria-label="Electrician at work" style="left:0;width:87px;background:linear-gradient(180deg,#4a3a30,#2a2520)"></div>
  <div class="abs slide" role="img" aria-label="Decorator with paint roller" style="left:108px;width:405px;background:linear-gradient(180deg,#7b6f63,#55504a 60%,#2e3432)"></div>
  <div class="abs slide" role="img" aria-label="Plasterer smoothing a ceiling" style="left:534px;width:404px;background:linear-gradient(180deg,#d9d4cc,#a39e96)"></div>
  <div class="abs slide" role="img" aria-label="Plumber fitting a kitchen tap" style="left:959px;width:241px;background:linear-gradient(180deg,#4d4a47,#1f1e1d)"></div>

  <svg class="abs arrow" style="left:41px;top:2462px" viewBox="0 0 32 32" fill="none" stroke="#fff" stroke-width="1.6"><circle cx="16" cy="16" r="14"/><path d="M22 16H10M15 11l-5 5 5 5"/></svg>
  <svg class="abs arrow" style="left:1126px;top:2462px" viewBox="0 0 32 32" fill="none" stroke="#fff" stroke-width="1.6"><circle cx="16" cy="16" r="14"/><path d="M10 16h12M17 11l5 5-5 5"/></svg>

  <span class="abs see" style="left:13px">See More</span>
  <span class="abs slide-label" style="left:108px">Painting &amp; Decorating</span>
  <span class="abs see" style="left:439px">See More</span>
  <span class="abs slide-label" style="left:534px">Plastering</span>
  <span class="abs see" style="left:864px">See More</span>
  <span class="abs slide-label" style="left:959px">Plumbing</span>

  <div class="abs dots" style="left:523px;top:2802px"><i class="on"></i><i></i><i></i><i></i><i></i><i></i></div>
</section>

<section class="abs testi">
  <h2>Hear from<br>Our Satisfied Clients</h2>
  <p class="lead">Our commitment to excellence has earned us the trust of numerous homeowners and businesses in London. Read their stories and understand the Brackwyn Group difference</p>
  <svg class="abs" style="left:75px;top:344px" width="42" height="42" viewBox="0 0 42 42" fill="none" stroke="#fff" stroke-width="1.6"><circle cx="21" cy="21" r="20"/><path d="M27 21H15M20 16l-5 5 5 5"/></svg>
  <p class="quote">“Lorem Ipsum is simply dummy text of the printing and typesetting industry. Lorem Ipsum has been the industry's standard dummy text ever since the 1500s”</p>
  <p class="who">Marla / Enterpreanure</p>
  <svg class="abs" style="left:1043px;top:344px" width="42" height="42" viewBox="0 0 42 42"><circle cx="21" cy="21" r="20" fill="#fff"/><path d="M15 21h12M22 16l5 5-5 5" fill="none" stroke="var(--teal)" stroke-width="1.6"/></svg>
  <div class="dots"><i></i><i></i><i class="on"></i><i></i><i></i><i></i></div>
</section>

<section class="abs contact">
  <h2>Contact Us</h2>
  <p>Ready to Start Your Project? Contact us today for a consultation and embark on the journey to turn your construction dreams into a stunning reality</p>
  <div class="btn start">Start Project
    <svg width="12" height="12" viewBox="0 0 12 12" fill="none" stroke="currentColor" stroke-width="1.5"><path d="M2 6h8M7 3l3 3-3 3"/></svg></div>
</section>

<footer>
  <div class="abs brand" style="left:60px;top:3858px"><span class="mark"></span>BRACKWYN</div>
  <p class="abs foot-about">Where Construction Meets Excellence.&nbsp; Based in London, we are committed to transforming your spaces into exceptional places.</p>
  <div class="abs socials"><i></i><i></i><i></i><i></i></div>
  <div class="abs foot-contacts">
    <span><svg viewBox="0 0 16 16" fill="none" stroke="currentColor" stroke-width="1.4"><rect x="1.5" y="3" width="13" height="10" rx="1"/><path d="M2 4l6 5 6-5"/></svg>brackwyn****@mailbox.com</span>
    <span><svg viewBox="0 0 16 16" fill="none" stroke="currentColor" stroke-width="1.4"><path d="M3 2h3l1.5 3.5-2 1.2a8 8 0 004 4l1.2-2L14 10v3a1 1 0 01-1 1A11 11 0 012 3a1 1 0 011-1z"/></svg>+44 20 *******</span>
    <span><svg viewBox="0 0 16 16" fill="none" stroke="currentColor" stroke-width="1.4"><path d="M8 15s5-5 5-8.5a5 5 0 00-10 0C3 10 8 15 8 15z"/><circle cx="8" cy="6.5" r="1.8"/></svg>London, UK</span>
  </div>
  <div class="abs foot-links">
    <span>Home</span><span>Project</span><span>Service</span>
    <span>About Us</span><span>Contact Us</span><span>FAQ</span>
  </div>
  <div class="abs rule" style="top:4118px"></div>
  <p class="abs copy">Brackwyn Group, Inc. © 2024 All Rights Reserved.</p>
  <div class="abs legal"><span>Privacy &amp; Policy</span><span>Terms &amp; Conditions</span></div>
</footer>

</body>
</html>
```